"Wild Spin Auntie" Comedy Tour needs show poster

I need a fun poster for my new comedy tour called "Wild Spin Auntie." This poster will be used by theaters and performing arts centers as well as on social media posts to promote the show.
Note: Please use 8.5"x11" dimensions for the poster. We would love vector images where possible in case the design needs to be scaled for social media.
Note: The poster will be used for different venues & dates, so you can put a lorem ipsum space for that somewhere on the poster.

Title Meaning:
If you do something "full send," you’re doing it it full-throttle and with 100% commitment—even if you end up failing - which can be funny. In extended, popular slang, full send has the sense of “intense,” “hardcore,” or “without regard to consequences.”
In terms of the comedy material in the show, I am a mom sending kids off to college and into the world. But I am also an athlete who does open water swimming, triathlons, snow skiing, etc. I think the poster would be funny showing a depiction of those activities (skiing, biking, or swimming) in a comical way.

It would be fun to have bright, retro colors & design elements from the 70s & 80s.
I am attaching some ski photos for that. "Full Send" or "Yard Sale" are both snow ski related too.
I am also attaching several photos/headshots that can be used in some way, but stylized (or just cut out the face part) as I am most interested in the graphics part of this poster. Maybe my face on a retro 80s skier body with bright colors?

Also, please note: I have always have great success here with very talented designers who know much more than me about the artwork. Please feel free to submit anything - I am open to suggestions and different interpretations. Thanks!!

Target Market(s)

Women ages 40+, Parents ages 30+, Couples ages 40+

Industry/Entity Type

Comedy, Entertainment

Requirements
Must have
• Tour Name (Wild Spin Auntie) & my name (Dana Whitlock)
Nice to have
• Would love to see a fun character in "Full Send" mode.
Should not have
• No trite references to motherhood (bottles, strollers, etc) or small children (my kids are grown). This poster is more about the fun and humor of "Full Send" in a comical way through skiiing, biking, or swimming .Please feel free to send questions!

```html
<!DOCTYPE html>
<html lang="en">
<head>
<meta charset="UTF-8">
<title>Wild Spin Auntie — Comedy Tour Poster</title>
<link href="https://fonts.googleapis.com/css2?family=Orbitron:wght@700;900&family=Montserrat:wght@400&display=swap" rel="stylesheet">
<style>
  :root {
    --bg: #000000;
    --ink: #ffffff;
    --neon-teal: #1fc7d4;
    --glow-pink: #c0307a;
    --glow-violet: #a02ab0;
    --glow-blue: #3a6fd8;
    --hair: #dccfae;
    --skin: #d9a88e;
    --shirt: #1f3f6e;
  }
  html, body {
    margin: 0;
    padding: 0;
    background: var(--bg);
    overflow: hidden;
  }
  .poster {
    position: relative;
    width: 800px;
    height: 1200px;
    overflow: hidden;
    background:
      radial-gradient(ellipse 190px 120px at 385px 770px, rgba(192,48,122,0.5), transparent 70%),
      radial-gradient(ellipse 330px 230px at 400px 720px, rgba(40,50,130,0.5), transparent 75%),
      var(--bg);
    color: var(--ink);
  }
  .edge-glow {
    position: absolute;
    top: 80px;
    width: 120px;
    height: 560px;
    filter: blur(22px);
    opacity: 0.85;
  }
  .edge-glow--left {
    left: -60px;
    background: linear-gradient(to bottom, transparent, var(--glow-pink) 25%, var(--glow-violet) 45%, var(--glow-blue) 75%, transparent);
  }
  .edge-glow--right {
    right: -60px;
    background: linear-gradient(to bottom, transparent, var(--glow-pink) 35%, var(--glow-blue) 75%, transparent);
  }
  .art {
    position: absolute;
    left: 0;
    top: 0;
  }
  .headline {
    font-family: 'Orbitron', sans-serif;
    font-weight: 900;
    fill: var(--ink);
  }
  .headline--slanted {
    font-style: italic;
  }
  .performer-box {
    fill: none;
    stroke: var(--ink);
    stroke-width: 3;
  }
  .schedule {
    position: absolute;
    left: 0;
    top: 1056px;
    width: 800px;
    margin: 0;
    text-align: center;
    font-family: 'Montserrat', sans-serif;
    font-size: 15.5px;
    line-height: 20px;
    font-weight: 400;
  }
</style>
</head>
<body>
  <main class="poster">
    <div class="edge-glow edge-glow--left"></div>
    <div class="edge-glow edge-glow--right"></div>

    <svg class="art" width="800" height="1200" viewBox="0 0 800 1200">
      <defs>
        <linearGradient id="portrait-tones" x1="0" y1="0" x2="0" y2="1">
          <stop offset="0" stop-color="var(--hair)"/>
          <stop offset="0.35" stop-color="var(--hair)"/>
          <stop offset="0.5" stop-color="var(--skin)"/>
          <stop offset="0.68" stop-color="var(--shirt)"/>
          <stop offset="1" stop-color="var(--shirt)"/>
        </linearGradient>
        <linearGradient id="portrait-fade" x1="0" y1="0" x2="0" y2="1">
          <stop offset="0.82" stop-color="#fff"/>
          <stop offset="1" stop-color="#000"/>
        </linearGradient>
        <mask id="portrait-mask">
          <rect x="0" y="0" width="800" height="560" fill="url(#portrait-fade)"/>
        </mask>
        <filter id="neon" x="-20%" y="-40%" width="140%" height="180%">
          <feGaussianBlur in="SourceAlpha" stdDeviation="5" result="blur"/>
          <feFlood flood-color="#1fc7d4" flood-opacity="0.95"/>
          <feComposite in2="blur" operator="in" result="glow"/>
          <feMerge>
            <feMergeNode in="glow"/>
            <feMergeNode in="glow"/>
            <feMergeNode in="SourceGraphic"/>
          </feMerge>
        </filter>
      </defs>

      <path role="img" aria-label="Cut-out headshot of the comedian: blonde hair, blue top, excited open-mouth expression"
            mask="url(#portrait-mask)" fill="url(#portrait-tones)"
            d="M300 150 C330 105 420 90 470 110 C530 135 555 200 560 245 C575 300 585 350 600 390 C640 400 665 420 680 470 L684 560 L120 560 L130 470 C140 425 175 410 200 400 C225 360 240 320 250 270 C260 215 275 180 300 150 Z"/>

      <g fill="#ffffff" opacity="0.8" aria-hidden="true">
        <circle cx="28" cy="640" r="1.5"/><circle cx="52" cy="865" r="1.2"/><circle cx="80" cy="900" r="1.6"/>
        <circle cx="58" cy="1000" r="2"/><circle cx="110" cy="950" r="1.2"/><circle cx="150" cy="1005" r="1.4"/>
        <circle cx="98" cy="730" r="1.3"/><circle cx="130" cy="840" r="1.1"/><circle cx="300" cy="1000" r="1"/>
        <circle cx="690" cy="640" r="2"/><circle cx="700" cy="690" r="1.4"/><circle cx="720" cy="760" r="1.2"/>
        <circle cx="740" cy="900" r="1.6"/><circle cx="710" cy="920" r="1.2"/><circle cx="765" cy="960" r="2.2"/>
        <circle cx="660" cy="980" r="1.3"/><circle cx="790" cy="700" r="1.2"/><circle cx="630" cy="820" r="1.6"/>
        <circle cx="380" cy="765" r="2.4"/><circle cx="290" cy="790" r="1.3"/><circle cx="560" cy="790" r="1.2"/>
        <circle cx="8" cy="950" r="1.5"/><circle cx="60" cy="840" r="1"/><circle cx="760" cy="1020" r="1"/>
      </g>

      <g filter="url(#neon)">
        <text class="headline headline--slanted" x="102" y="600" font-size="72" textLength="566" lengthAdjust="spacingAndGlyphs">WILD SPIN</text>
        <text class="headline" x="115" y="732" font-size="146" textLength="535" lengthAdjust="spacingAndGlyphs">AUNTIE</text>
        <text class="headline" x="180" y="830" font-size="44" textLength="440" lengthAdjust="spacingAndGlyphs">COMEDY TOUR</text>
        <text class="headline" x="318" y="882" font-size="46" textLength="164" lengthAdjust="spacingAndGlyphs">WITH</text>
        <rect class="performer-box" x="162" y="912" width="476" height="48"/>
        <text class="headline" x="205" y="945" font-size="24" textLength="390" lengthAdjust="spacing">DANA WHITLOCK</text>
        <text class="headline" x="115" y="1025" font-size="22" textLength="565" lengthAdjust="spacingAndGlyphs">ENTRY $15 // ALL NIGHT // FREE PARKING</text>
      </g>
    </svg>

    <p class="schedule">Lorem ipsum dolor sit amet, consectetuer adipiscing elit, sed<br>diam nonummy nibh euismod.</p>
  </main>
</body>
</html>
```